Hip and quirky Indian restaurant Menu

We need a build your own bowl/meal/wrap menu similar to Marwenda others. We would like illustrations if possible of India/veggies/chicken/animals/themes. Please utilize the colors that match the schema of the logos provided. We have included pictures you may use them if you would like to. Menu provided is our old menu.

Target Market(s)

Millenials, Ge

Industry/Entity Type

Retail

Font styles to use
Sans Serif
Decorative

Requirements
Must have
• logical placements for build your own meal options
Nice to have
• Illustrations.

```html
<!DOCTYPE html>
<html lang="en">
<head>
<meta charset="utf-8">
<title>Tiffin Lane Menu</title>
<link href="https://fonts.googleapis.com/css2?family=Roboto+Condensed:ital,wght@0,400;0,700;1,400;1,700&display=swap" rel="stylesheet">
<style>
:root{
  --orange:#f26a3f;
  --yellow:#fbb040;
  --red:#e8262f;
  --navy:#2b2a6b;
  --maroon:#6e1c1c;
  --white:#ffffff;
}
*{box-sizing:border-box;margin:0;padding:0}
html,body{width:1200px;height:848px;overflow:hidden;background:#fff}
body{font-family:"Roboto Condensed",sans-serif;color:var(--maroon)}
.menu{position:relative;width:1200px;height:848px;overflow:hidden;background:var(--white)}
.abs{position:absolute}
.wave{position:absolute;left:0;top:0}
.photo{position:absolute;border-radius:50%}
.brand{left:30px;top:60px;width:140px;text-align:center}
.brand-circle{width:34px;height:34px;border-radius:50%;background:var(--yellow);margin:0 auto 8px}
.brand-name{font-weight:700;font-size:30px;line-height:30px;color:var(--red)}
.headline{position:absolute;font-weight:700;white-space:nowrap;transform-origin:left top;line-height:1}
.title-build{left:292px;top:100px;font-size:33px;color:var(--navy);transform:scaleX(.86)}
.title-meal{left:243px;top:132px;font-size:44px;color:var(--navy);transform:scaleX(.8)}
.price-dot{display:flex;align-items:center;justify-content:center;border-radius:50%;font-weight:700;color:#fff;z-index:2}
.step-num{font-weight:700;font-size:62px;line-height:62px;color:var(--orange)}
.bar{position:absolute;background:var(--orange);font-size:20px;line-height:28px;padding-left:18px;color:var(--maroon);white-space:nowrap}
.bar b{font-weight:700;color:#fff}
.bar i{font-weight:700;font-size:14px;color:var(--maroon)}
.card{position:absolute;background:#fff;padding:7px 0 0 18px;font-weight:700;font-size:13px;line-height:17.5px;white-space:nowrap}
.card .col{position:absolute;top:7px}
.k,.v{display:inline-block;width:8px;height:8px;border-radius:50%;color:#fff;font-size:6px;line-height:8px;text-align:center;vertical-align:1px;margin-left:2px;font-weight:700;background:var(--orange)}
.hot{display:inline-block;width:9px;height:4px;border-radius:4px;background:var(--red);transform:rotate(-40deg);margin-left:2px;vertical-align:2px}
.small{font-weight:400;font-size:9px}
.note{font-weight:400;font-size:9.5px}
.trad{color:#fff}
.dish-head{position:absolute;background:var(--navy);color:#fff;font-weight:700;font-size:15px;line-height:24px;padding-left:14px}
.right{position:absolute;left:723px;top:0;width:477px;height:848px;background:var(--navy)}
.box{position:absolute;background:#fff}
.box h3{background:var(--orange);color:#fff;font-weight:700;font-size:15px;line-height:25px;padding-left:14px}
.list{padding:8px 12px 0 14px;font-weight:700;font-size:12.5px;line-height:19.6px;color:var(--navy);white-space:nowrap}
.row{display:flex;align-items:baseline}
.row .fill{flex:1;border-bottom:1px dotted #777;margin:0 2px;transform:translateY(-3px);min-width:4px}
.row .p2{width:38px;text-align:right}
.biri{position:absolute;left:876px;top:227px;width:297px;height:109px;background:var(--orange);padding:8px 0 0 44px;color:#fff;font-weight:700;font-size:12.5px;line-height:19.8px;white-space:nowrap}
.biri .row .fill{border-color:#fff}
.rice-note{position:absolute;left:876px;top:339px;width:297px;height:64px;background:var(--yellow);padding:5px 0 0 14px;color:var(--maroon);white-space:nowrap}
.legend{position:absolute;left:1023px;top:606px;color:#fff;font-size:9.5px;line-height:16px;font-weight:700;z-index:3}
.food-corner{position:absolute;left:960px;top:668px;width:260px;height:200px;border-radius:100% 0 0 0 / 60% 0 0 0;background:radial-gradient(circle at 45% 60%,#c9552a,#8a3a1e 45%,#5a7a2a 75%,#2b2a6b);z-index:1}
.contact{position:absolute;left:723px;top:698px;width:250px;height:122px;background:linear-gradient(90deg,#3b3c9a,#4a4ab0 75%,rgba(74,74,176,0));color:#fff;z-index:2;white-space:nowrap}
</style>
</head>
<body>
<main class="menu">

  <svg class="wave" width="723" height="848" viewBox="0 0 723 848" aria-hidden="true">
    <path d="M0 176 C60 150 120 170 180 196 C260 230 330 260 420 270 C520 280 560 360 560 420 C600 470 680 480 723 470 L723 591 L0 591 Z" fill="var(--yellow)"/>
    <path d="M0 591 L600 591 Q690 591 690 660 L690 848 L0 848 Z" fill="var(--red)"/>
    <path d="M690 591 L723 591 L723 848 L690 848 Z" fill="var(--yellow)"/>
    <path d="M420 0 C440 60 520 120 620 150 C670 165 700 185 723 195" stroke="var(--navy)" stroke-width="2" fill="none"/>
  </svg>
  <div class="photo" role="img" aria-label="Overhead photo of curry dishes, rice and samosas on a table" style="left:486px;top:-20px;width:250px;height:165px;border-radius:45% 20% 40% 55%;background:radial-gradient(circle at 40% 50%,#c58a3a,#6b4a2a 70%,#3a2a1e)"></div>

  <div class="abs brand">
    <div class="brand-circle"></div>
    <div class="brand-name">TIFFIN<br>LANE</div>
  </div>

  <div class="headline title-build">Build Your</div>
  <div class="headline title-meal">OWN MEAL</div>
  <div class="abs price-dot" style="left:427px;top:108px;width:58px;height:58px;background:var(--red);font-size:24px">7.00</div>

  <div class="photo" role="img" aria-label="Bowl of yellow basmati rice" style="left:190px;top:195px;width:144px;height:144px;background:radial-gradient(circle,#f6e4a8,#e9c45a 60%,#9a9a9a)"></div>
  <div class="photo" role="img" aria-label="Bowl of curry with vegetables" style="left:519px;top:195px;width:144px;height:144px;background:radial-gradient(circle,#d9582a,#b8441f 55%,#e8e1d2)"></div>
  <div class="photo" role="img" aria-label="Bowl of green bean and carrot salad" style="left:190px;top:366px;width:144px;height:144px;background:radial-gradient(circle,#c9a63a,#6f8a3a 60%,#3a3a3a)"></div>
  <div class="photo" role="img" aria-label="Bowl of dipping sauce" style="left:519px;top:405px;width:144px;height:144px;background:radial-gradient(circle,#b79a56,#6b5a35 60%,#3a3020)"></div>

  <div class="abs step-num" style="left:40px;top:222px">1</div>
  <div class="bar" style="left:42px;top:268px;width:312px;height:28px">Pick <b>Meal</b></div>
  <div class="card" style="left:42px;top:296px;width:312px;height:65px">
    Salad Bowl (Keto friendly)<br>Rice Bowl (Curry or Plain)<br>Wrap (Naan or Paratha)
  </div>

  <div class="abs step-num" style="left:370px;top:222px">2</div>
  <div class="bar" style="left:373px;top:268px;width:313px;height:28px">Pick <b>Main Curry</b> <i>(Pick one)</i></div>
  <div class="card" style="left:373px;top:296px;width:313px;height:100px">
    <div class="col" style="left:18px">Veg Korma <span class="v">V</span><br>Chana Masala <span class="v">V</span><br>Chicken Tikka Masala <span class="k">K</span><br>Chili Chicken <span class="k">K</span><span class="hot"></span><br>Tandoori Chicken <span class="k">K</span> <span class="small">(3 Pcs.)</span></div>
    <div class="col" style="left:181px">Beef Curry <span class="k">K</span><span class="hot"></span><span style="position:absolute;left:98px">*+1</span><br>Mutton Curry <span class="k">K</span><span style="position:absolute;left:98px">*+2</span><br>Double Protein<span style="position:absolute;left:98px">*+2</span><br><span class="note" style="position:relative;top:-3px">*(For premium curry extra)</span></div>
  </div>

  <div class="abs step-num" style="left:38px;top:396px">3</div>
  <div class="bar" style="left:42px;top:441px;width:312px;height:28px">Pick <b>Toppings</b> <i>(Pick as many)</i></div>
  <div class="card" style="left:42px;top:469px;width:312px;height:100px">
    <div class="col" style="left:18px">Beets Thoran <span class="v">V</span><br>Green Beans Thoran <span class="v">V</span><br>Cabbage Thoran <span class="k">K</span><span class="v">V</span><br>Chick Pea Salad <span class="k">K</span><span class="v">V</span><br>Cucumber Salad <span class="k">K</span><span class="v">V</span></div>
    <div class="col" style="left:169px">Diced Onion <span class="v">V</span><br>Chopped Bell Pepper <span class="v">V</span><br>Shredded Cheese <span class="k">K</span><br>Cilantro <span class="k">K</span><span class="v">V</span><br>Jalapeno <span class="k">K</span><span class="v">V</span></div>
  </div>

  <div class="abs step-num" style="left:370px;top:432px">4</div>
  <div class="bar" style="left:373px;top:479px;width:313px;height:28px">Pick <b>Sauces</b> <i>(Pick as many)</i></div>
  <div class="card" style="left:373px;top:507px;width:313px;height:62px">
    <div class="col" style="left:18px">Original Mint <span class="k">K</span><span class="v">V</span><br>Sweet Tamarind <span class="k">K</span><span class="v">V</span><br>Cool Yogurt <span class="k">K</span></div>
    <div class="col" style="left:185px">Mango Chilli <span class="k">K</span><span class="v">V</span><span class="hot"></span><br>Tikka Masala <span class="k">K</span><span class="v">V</span></div>
  </div>

  <div class="headline trad" style="left:237px;top:616px;font-size:37px;transform:scaleX(.8)">Traditional</div>
  <div class="headline trad" style="left:278px;top:650px;font-size:46px;transform:scaleX(.84)">BOWL</div>
  <div class="abs price-dot" style="left:382px;top:626px;width:58px;height:58px;background:var(--navy);font-size:24px">7.00</div>

  <div class="abs step-num" style="left:93px;top:610px;color:var(--yellow)">1</div>
  <div class="bar" style="left:94px;top:658px;width:157px;height:29px;background:var(--yellow);padding-left:19px">Pick <b style="color:#fff">Main</b></div>
  <div class="card" style="left:94px;top:687px;width:157px;height:31px;padding:6px 0 0 19px">Rice , Naan, Paratha</div>

  <div class="abs step-num" style="left:42px;top:676px;color:var(--yellow)">2</div>
  <div class="bar" style="left:45px;top:727px;width:276px;height:28px;background:var(--yellow)">Pick <b>Curries</b></div>
  <div class="card" style="left:45px;top:755px;width:276px;height:74px;font-weight:400">
    Your choice of <b>1 Veg</b> &amp; <b>1 Meat</b> Dish
    <div style="margin-top:16px;font-weight:700">Additional Dish <span style="margin-left:14px">+2</span></div>
    <div class="note" style="line-height:10px;font-style:italic">(Premium dishes are extra.)</div>
  </div>

  <div class="dish-head" style="left:336px;top:708px;width:168px">Veg Dishes</div>
  <div class="card" style="left:336px;top:732px;width:168px;height:97px;padding-left:14px">
    Chana Masala <span class="v">V</span><br>Veg Korma <span class="v">V</span><br>Cabbage Thoran <span class="k">K</span><span class="v">V</span><br>Beets Thoran <span class="v">V</span><br>Green Beans Thoran <span class="v">V</span>
  </div>
  <div class="dish-head" style="left:513px;top:708px;width:169px">Meat Dishes</div>
  <div class="card" style="left:513px;top:732px;width:169px;height:97px;padding-left:14px">
    Chicken Tikka Masala <span class="k">K</span><br>Chilli Chicken <span class="k">K</span><span class="hot"></span><br>Tandoori Chicken <span class="k">K</span> <span class="small">(3 Pcs.)</span><br>Beef Curry <span class="k">K</span><span class="hot"></span><span style="position:absolute;left:140px">+1</span><br>Mutton Curry <span class="k">K</span><span style="position:absolute;left:140px">+2</span>
  </div>

  <div class="right"></div>

  <div class="box" style="left:750px;top:30px;width:149px;height:171px">
    <h3>Snacks</h3>
    <div class="list" style="padding-top:14px">
      <div class="row">Samosa<span class="fill"></span>1.00</div>
      <div class="row">Veg Puffs<span class="fill"></span>1.49</div>
      <div class="row">Egg Puffs<span class="fill"></span>2.49</div>
      <div class="row">Sweet Puffs<span class="fill"></span>1.49</div>
      <div class="row">Beef Puffs<span class="fill"></span>1.49</div>
      <div class="row">Chicken Puffs<span class="fill"></span>1.49</div>
    </div>
  </div>

  <div class="box" style="left:906px;top:30px;width:267px;height:171px">
    <h3>Lassi / Indian Yogurt Shakes</h3>
    <span style="position:absolute;left:141px;top:31px;font-size:10.5px;color:var(--orange);font-style:italic">S (12oz)</span>
    <span style="position:absolute;left:194px;top:31px;font-size:10.5px;color:var(--orange);font-style:italic">L (20oz)</span>
    <div class="list" style="padding:13px 47px 0 14px">
      <div class="row">Original Lassi<span class="fill"></span>2.00<span class="p2">2.50</span></div>
      <div class="row">Mango Lassi<span class="fill"></span>2.50<span class="p2">3.00</span></div>
      <div class="row">Rose Lassi<span class="fill"></span>2.50<span class="p2">3.00</span></div>
      <div class="row">Chai Spice Lassi<span class="fill"></span>2.50<span class="p2">3.00</span></div>
      <div class="row">Cookies N Cream Lassi<span class="fill"></span>2.50<span class="p2">3.00</span></div>
      <div class="row">Chocolate Hazelnut<span class="fill"></span>2.50<span class="p2">3.00</span></div>
    </div>
  </div>
  <div class="abs" role="img" aria-label="Glass of mango lassi" style="left:1133px;top:108px;width:52px;height:102px;border-radius:8px 8px 40% 40%;background:linear-gradient(180deg,#f8d24a,#f0b020)"></div>

  <div class="biri">
    <div class="row">Chicken Biriyani Bowl<span class="fill"></span>7.00</div>
    <div class="row">Mutton Biriyani Bowl<span class="fill"></span>10.00</div>
    <div class="row">Boneless Chicken Biriyani<span class="fill"></span>10.00</div>
    <div class="row">Boneless Lamb Biriyani<span class="fill"></span>14.00</div>
    <div class="row">Vegetable Biriyani<span class="fill"></span>8.00</div>
  </div>
  <div class="rice-note">
    <div style="font-weight:700;font-size:15px;line-height:18px">“The Original Indian Rice Bowl!</div>
    <div style="font-style:italic;font-size:11px;line-height:14px">Meat and rice which has been baked to perfection.”</div>
    <div style="font-weight:700;font-size:12px;line-height:20px">Served with yogurt sauce, pickle &amp; pappadom.</div>
  </div>
  <div class="photo" role="img" aria-label="Plate of chicken biriyani" style="left:789px;top:207px;width:120px;height:120px;background:radial-gradient(circle,#e3a84a,#c07a2a 65%,#8a6a3a)"></div>
  <div class="photo" role="img" aria-label="Plate of mutton biriyani" style="left:762px;top:300px;width:114px;height:114px;background:radial-gradient(circle,#e6b04e,#b8702a 65%,#4a4a5a)"></div>

  <div class="box" style="left:750px;top:421px;width:257px;height:83px">
    <h3>Chicken Meals</h3>
    <div class="list" style="padding-top:9px">
      <div class="row">Tandoori Chicken / Fries&nbsp;<span class="small">(5 Pcs.)</span><span class="fill"></span>7.00</div>
      <div class="row">Spicy Chicken Tender / Fries&nbsp;<span class="small">(4 Pcs.)</span><span class="fill"></span>7.00</div>
    </div>
  </div>

  <div class="box" style="left:750px;top:513px;width:257px;height:82px">
    <h3>Loaded Fries</h3>
    <div class="list" style="padding-top:10px">
      <div class="row">Chicken Tikka Fries<span class="fill"></span>6.00</div>
      <div class="row">Chili Chicken Fries<span class="fill"></span>6.00</div>
    </div>
  </div>

  <div class="box" style="left:750px;top:603px;width:182px;height:77px">
    <h3>Dessert</h3>
    <div class="list" style="padding-top:10px">
      <div class="row">Mango Pudding<span class="fill"></span>3.50</div>
      <div class="row">Rice Pudding<span class="fill"></span>3.50</div>
    </div>
  </div>

  <div class="box" style="left:1014px;top:421px;width:159px;height:163px">
    <h3>Drinks</h3>
    <div class="list" style="padding-top:9px">
      <div class="row">Iced Tea&nbsp;<span style="color:var(--orange);font-weight:400;font-size:10px">32oz</span><span class="fill"></span>2.00</div>
      <div class="row">Lemonade&nbsp;<span style="color:var(--orange);font-weight:400;font-size:10px">32oz</span><span class="fill"></span>3.00</div>
      <div class="row">Masala Tea<span class="fill"></span>2.00</div>
      <div class="row">Indian Coffee<span class="fill"></span>2.00</div>
      <div class="row">Soda Can<span class="fill"></span>1.00</div>
      <div class="row">Water Bottle<span class="fill"></span>1.00</div>
    </div>
  </div>

  <div class="legend">
    <div><span class="k" style="width:11px;height:11px;line-height:11px;font-size:7px">K</span> - KETO <span style="margin-left:26px"><span class="hot"></span> - SPICY</span></div>
    <div><span class="v" style="width:11px;height:11px;line-height:11px;font-size:7px">V</span> - VEGAN</div>
    <div style="font-size:12px;font-weight:400">All meat is halal.</div>
  </div>

  <div class="food-corner" role="img" aria-label="Grilled tandoori chicken with lemon, cilantro and chilli powder"></div>

  <div class="contact">
    <div style="position:absolute;left:16px;top:5px;font-weight:700;font-size:18px">TIFFIN LANE</div>
    <div style="position:absolute;left:19px;top:36px;font-size:12px">412 W Harlow Ave, Brookdale, TX 75300</div>
    <div style="position:absolute;left:19px;top:50px;font-size:21px">555-014-2290</div>
    <div style="position:absolute;left:19px;top:78px;font-weight:700;font-size:14px;color:var(--yellow)">Tue-Sat : 11 am - 7 pm</div>
    <div style="position:absolute;left:47px;top:100px;font-weight:700;font-size:14px;color:var(--yellow)">Sun : 11 am - 6 pm</div>
  </div>

</main>
</body>
</html>
```